Updated brief for New ecommerce site needs a stunning business card that links to web site.

Updated business card brief. Please refer to the new files uploaded today (the last two) which show the background colour/style that we will be using in our web template for on-line trading, the grey marble concrete look.

Please see if you can use the grey marble background in the business card design in a way so it relates to our web template. It also needs to be transferable to banner ad, chatterbox ad etc.
vantor hub is a NEW eCommerce website which is commencing selling via bidnook & swapcrate, used & damaged mobile phones & accessories, evolving into a full eCommerce store.

We like strong clean lines, use of a circle, in essence this will become our logo as well. Colours strong orange/Black/White The orange stronger than in PixelHerd #8164937 & grey marble as per file attached #274615

We love the use of a circle!! As we are evolving & moving forward this is what the circle represents to us……. ongoing change.

Front side with a circle with vantor hub in a modern font in the middle, vantor is in a strong orange and group is in black or white. On the reverse side, use layout as per Snapwell design from plonk.com. for icon details (not the boarder at top/botto).

This design is to meet www.plonk.com luxe cards specifications
Thank you we look forward to last minute inspiration.

Project Deadline Extended Reason: Hi We need to extend our deadline to ensure we don't rush the design. We are close to getting what we want, however due to work commitments here we need a couple more days to work this through to ensure the concept ties in with our other marketing.Thank you for understanding and your patience.vantorhub Added Tuesday, March 3, 2015

Target Market(s)

Suppliers & business networking

Industry/Entity Type

Business

Contact Information for Business Card

Liam Presk
Director
mob +61 4987 6543
Locked Bag WXYZ 5678 QRS
liam@vantorhub.example.au
www.vantorhub.example.au

Requirements
Must have
• Design to meet www.plonk.com luxe business card specifications
• Colours - orange needs to be bold and strong & /black/white
• Circle with vantor hub in the middle
Nice to have
• Grey marble background incorporated into design in someway so it links with our web page.

```html
<!DOCTYPE html>
<html lang="en">
<head>
<meta charset="utf-8">
<title>vantor hub — business card</title>
<link rel="stylesheet" href="https://fonts.googleapis.com/css2?family=Oswald:wght@500;600&family=Open+Sans:wght@400&display=swap">
<style>
  :root {
    --backdrop: #d9d4cf;
    --orange: #f39325;
    --card-black: #232223;
    --circle-black: #262526;
    --arc-grey: #2e2d2e;
    --white: #ffffff;
    --text-soft: #e6e6e6;
  }
  * { margin: 0; padding: 0; box-sizing: border-box; }
  html, body {
    width: 1200px;
    height: 800px;
    overflow: hidden;
    background: var(--backdrop);
  }
  .sheet {
    width: 1200px;
    height: 800px;
    display: flex;
    align-items: center;
    justify-content: center;
    gap: 60px;
  }
  .card {
    position: relative;
    width: 520px;
    height: 336px;
    overflow: hidden;
    box-shadow: 0 10px 24px rgba(60, 50, 40, 0.18);
  }
  .card-front {
    background: var(--orange);
    display: flex;
    align-items: center;
    justify-content: center;
  }
  .brand-circle {
    width: 262px;
    height: 262px;
    border-radius: 50%;
    background: var(--circle-black);
    display: flex;
    align-items: center;
    justify-content: center;
  }
  .brand-name {
    font-family: "Oswald", sans-serif;
    font-weight: 600;
    font-size: 46px;
    letter-spacing: 1px;
    color: var(--orange);
    line-height: 1;
  }
  .card-back {
    background: var(--card-black);
  }
  .card-back .arcs {
    position: absolute;
    inset: 0;
  }
  .contact-block {
    position: absolute;
    left: 150px;
    top: 62px;
    color: var(--text-soft);
  }
  .person-name {
    font-family: "Oswald", sans-serif;
    font-weight: 600;
    font-size: 34px;
    letter-spacing: 1.5px;
    color: var(--white);
    line-height: 1.05;
  }
  .person-title {
    font-family: "Oswald", sans-serif;
    font-weight: 600;
    font-size: 24px;
    letter-spacing: 2px;
    color: var(--orange);
    line-height: 1.1;
    margin-bottom: 20px;
  }
  .contact-list {
    list-style: none;
    font-family: "Open Sans", sans-serif;
    font-size: 13px;
    line-height: 1.85;
  }
</style>
</head>
<body>
<main class="sheet">
  <section class="card card-front" aria-label="Business card front">
    <div class="brand-circle">
      <span class="brand-name">vantor hub</span>
    </div>
  </section>

  <section class="card card-back" aria-label="Business card back">
    <svg class="arcs" width="520" height="336" viewBox="0 0 520 336" aria-hidden="true">
      <circle cx="40" cy="-40" r="150" fill="var(--arc-grey)"/>
      <circle cx="470" cy="380" r="190" fill="var(--arc-grey)"/>
    </svg>
    <div class="contact-block">
      <h1 class="person-name">Liam Presk</h1>
      <p class="person-title">DIRECTOR</p>
      <ul class="contact-list">
        <li>Locked Bag WXYZ 5678 QRS</li>
        <li>mob +61 4987 6543</li>
        <li>liam@vantorhub.example.au</li>
        <li>www.vantorhub.example.au</li>
      </ul>
    </div>
  </section>
</main>
</body>
</html>
```